Homemaking training schools needs a Business Card design

Designer, Hello!

No special requirements, good-looking enough.
--------------------------------------------------------------------------

Name: Marcus Liao
Chairman
Tel: 0574-57418263
Mobile: 13852247106
Email: kelvory@mailpond.com
Web: www.tqb2031.com
Add: No.258, LinfengJie, DaoyueQu, Ningbo, Zhejiang

LOGO
Ningbo TQB Homemaking Training School

Target Market(s)

pregnant women, mothers, infants, the elderly and families, including cleaning, cooking, nursing training.

Industry/Entity Type

Business

Contact Information for Business Card

Name: Marcus Liao
Chairman
Tel: 0574-57418263
Mobile: 13852247106
Email: kelvory@mailpond.com
Web: www.tqb2031.com

LOGO

Font styles to use
Serif
Sans Serif
Decorative

Requirements
Nice to have
• Feels: clean, specifications, safety, comfort, warmth and happiness.

```html
<!DOCTYPE html>
<html lang="en">
<head>
<meta charset="utf-8">
<title>TianQiBao Business Card</title>
<link href="https://fonts.googleapis.com/css2?family=Montserrat:wght@500;600;800&family=Quicksand:wght@400;600&display=swap" rel="stylesheet">
<style>
  :root {
    --brand-blue: #1a73bf;
    --brand-pink: #e8088a;
    --ink-dark: #2b2b2b;
    --band-grey: #3d3d3d;
    --paper: #ffffff;
    --backdrop: #e9eaec;
    --soft-pink: #fbe3ef;
  }
  * { margin: 0; padding: 0; box-sizing: border-box; }
  html, body { width: 1200px; height: 900px; overflow: hidden; }
  body {
    background: var(--backdrop);
    position: relative;
    font-family: "Montserrat", sans-serif;
  }
  .card {
    position: absolute;
    width: 640px;
    height: 365px;
    border-radius: 26px;
    overflow: hidden;
    box-shadow: 0 10px 28px rgba(0,0,0,.18);
  }
  /* Back side */
  .card-back { left: 80px; top: 60px; background: var(--brand-blue); }
  .back-mark {
    position: absolute; left: 60px; bottom: 70px;
    display: flex; align-items: center; gap: 14px;
  }
  .back-mark .dot { width: 46px; height: 46px; border-radius: 50%; background: var(--brand-pink); }
  .back-mark .name {
    font-family: "Quicksand", sans-serif; font-weight: 600;
    font-size: 40px; color: var(--paper);
  }
  .back-web {
    position: absolute; right: 60px; bottom: 74px;
    font-weight: 600; font-size: 20px; color: var(--paper);
  }
  .back-web .accent { color: var(--brand-pink); }

  /* Front side */
  .card-front { left: 480px; top: 475px; background: var(--paper); }
  .front-bands { position: absolute; inset: 0; }
  .soft-circle {
    position: absolute; right: 70px; top: 18px;
    width: 90px; height: 90px; border-radius: 50%; background: var(--soft-pink);
  }
  .holder { position: absolute; left: 34px; top: 58px; }
  .holder-name {
    font-weight: 800; font-size: 27px; color: var(--brand-blue); letter-spacing: .5px;
  }
  .holder-title {
    font-weight: 800; font-size: 13px; color: var(--brand-pink); letter-spacing: 1px;
  }
  .wordmark {
    position: absolute; left: 190px; top: 120px; width: 260px; text-align: center;
  }
  .wordmark-row { display: flex; align-items: center; justify-content: center; gap: 8px; }
  .wordmark .dot { width: 14px; height: 14px; border-radius: 50%; background: var(--brand-pink); }
  .wordmark-name {
    font-family: "Quicksand", sans-serif; font-weight: 600;
    font-size: 44px; color: var(--brand-blue); line-height: 1.1;
  }
  .tagline {
    display: flex; align-items: center; gap: 8px; margin-top: 4px;
    font-family: "Quicksand", sans-serif; font-size: 16px; color: var(--ink-dark);
  }
  .tagline::before, .tagline::after { content: ""; flex: 1; height: 1px; background: var(--ink-dark); }
  .contacts {
    position: absolute; right: 22px; top: 108px;
    list-style: none; text-align: right;
  }
  .contacts li {
    display: flex; justify-content: flex-end; align-items: center; gap: 6px;
    font-weight: 600; font-size: 13px; color: var(--ink-dark); line-height: 20px;
  }
  .contacts svg { width: 12px; height: 12px; fill: none; stroke: var(--brand-blue); stroke-width: 2; }
  .address {
    position: absolute; left: 34px; bottom: 14px;
    font-weight: 600; font-size: 13px; color: var(--paper); line-height: 17px;
  }
</style>
</head>
<body>
  <section class="card card-back" aria-label="Card back">
    <div class="back-mark"><span class="dot"></span><span class="name">TianQiBao</span></div>
    <div class="back-web">www.<span class="accent">tqb2031</span>.com</div>
  </section>

  <section class="card card-front" aria-label="Card front">
    <div class="soft-circle"></div>
    <svg class="front-bands" viewBox="0 0 640 365" aria-hidden="true">
      <polygon points="0,312 330,312 352,262 410,262 470,365 0,365" fill="var(--brand-blue)"/>
      <line x1="418" y1="246" x2="640" y2="246" stroke="var(--brand-pink)" stroke-width="3"/>
      <polygon points="424,254 640,254 640,292 446,292" fill="var(--band-grey)"/>
    </svg>

    <div class="holder">
      <div class="holder-name">MARCUS LIAO</div>
      <div class="holder-title">CHAIRMAN</div>
    </div>

    <div class="wordmark">
      <div class="wordmark-row"><span class="dot"></span><span class="wordmark-name">TianQiBao</span></div>
      <div class="tagline">Training &amp; Services</div>
    </div>

    <ul class="contacts">
      <li>0574-57418263
        <svg viewBox="0 0 12 12"><path d="M2 1h3l1 3-2 1a6 6 0 0 0 3 3l1-2 3 1v3c-6 0-9-3-9-9z"/></svg></li>
      <li>13852247106
        <svg viewBox="0 0 12 12"><rect x="3" y="1" width="6" height="10" rx="1"/></svg></li>
      <li>kelvory@mailpond.com
        <svg viewBox="0 0 12 12"><rect x="1" y="2.5" width="10" height="7"/><path d="M1 3l5 4 5-4"/></svg></li>
      <li>www.tqb2031.com
        <svg viewBox="0 0 12 12"><circle cx="6" cy="6" r="5"/><path d="M1 6h10M6 1c-3 3-3 7 0 10M6 1c3 3 3 7 0 10"/></svg></li>
    </ul>

    <address class="address" style="font-style:normal">
      258, LinfengJie<br>DaoyueQu, Ningbo, Zhejiang
    </address>
  </section>
</body>
</html>
```